Business Card Design Project

I have had my current business card for 6years and it is time to upgrade my business card. I have uploaded my old card
I am a retail specialty shop designer and want something designer looking but professional.
Target Market(s)
30-60 year old people in retail businesses
Industry/Entity Type
Retail
Requirements
Must have
- The Maple Fitouts logo (but colour can and style can be altered)
My name, position and contact details as per my existing card attached .
Rowan Pellicott Director
m: 0418593417
rowan@maplefitouts-example.com.au
www.maplefitouts-example.com.au
t:02 95318274 f: 02 95318291
po box 871 kestrel bay nsw 2099
Nice to have
- Use both sides of the card

```html
<!DOCTYPE html>
<html lang="en">
<head>
<meta charset="utf-8">
<title>Maple Fitouts – Business Card</title>
<link rel="stylesheet" href="https://fonts.googleapis.com/css2?family=Questrial&family=Merriweather:wght@700&family=Arimo:wght@400&display=swap">
<style>
  :root {
    --bg: #e4e4e4;
    --yellow-light: #f8c51e;
    --yellow-deep: #eea300;
    --brown: #6b4310;
    --white: #ffffff;
    --silver-light: #f4eee6;
    --silver-dark: #b9a58a;
  }
  * { box-sizing: border-box; margin: 0; padding: 0; }
  html, body { width: 1200px; height: 951px; overflow: hidden; }
  body { background: var(--bg); position: relative; font-family: "Arimo", sans-serif; }

  .card {
    position: absolute;
    width: 580px;
    height: 350px;
    overflow: hidden;
    box-shadow: 0 10px 28px rgba(0,0,0,0.25);
  }

  /* Front */
  .card--front { left: 60px; top: 60px;
    background: radial-gradient(ellipse at 40% 40%, var(--yellow-light), var(--yellow-deep) 85%); }
  .card__texture { position: absolute; inset: 0;
    background: linear-gradient(160deg, rgba(255,255,255,0.08), rgba(0,0,0,0.04)); }
  .card__edge { position: absolute; top: 0; bottom: 0; width: 22px;
    background: linear-gradient(90deg, var(--silver-dark), var(--silver-light) 50%, var(--silver-dark)); }
  .card__edge--left { left: 0; }
  .card__edge--right { right: 0; }

  .brand {
    position: absolute;
    display: flex; align-items: center; gap: 12px;
    font-family: "Questrial", sans-serif;
    text-transform: uppercase; letter-spacing: 2px; white-space: nowrap;
  }
  .brand__mark { width: 14px; height: 14px; flex: none; }
  .card--front .brand { left: 0; right: 0; top: 130px; justify-content: center;
    font-size: 38px; color: var(--white); }
  .card--front .brand__mark { background: var(--white); }

  .front__url { position: absolute; left: 0; right: 0; top: 272px; text-align: center;
    font-size: 19px; color: var(--brown); letter-spacing: 0.5px; }

  /* Back */
  .card--back { left: 580px; top: 520px;
    background: radial-gradient(ellipse at 30% 40%, var(--yellow-light), var(--yellow-deep) 90%); }
  .back__panel { position: absolute; top: 0; right: 0; width: 230px; height: 100%; }
  .card--back .brand { right: 22px; top: 162px; font-size: 21px; color: var(--brown); gap: 8px; }
  .card--back .brand__mark { width: 11px; height: 11px; background: var(--brown); }

  .contact__name { position: absolute; left: 30px; top: 20px;
    font-family: "Merriweather", serif; font-weight: 700; font-size: 21px; color: var(--white); }
  .contact__role { position: absolute; left: 30px; top: 50px; font-size: 12px; color: var(--brown); }

  .contact__address { position: absolute; left: 30px; top: 96px; display: flex; gap: 10px;
    font-size: 14px; color: var(--brown); line-height: 1.3; }
  .contact__list { position: absolute; left: 30px; top: 170px; list-style: none;
    font-size: 14px; color: var(--brown); line-height: 1.25; }
  .contact__list li { display: flex; align-items: center; gap: 10px; }
  .icon { width: 14px; height: 14px; flex: none; fill: var(--brown); }
  .icon--blank { visibility: hidden; }
</style>
</head>
<body>

<section class="card card--front" aria-label="Business card front">
  <div class="card__texture" role="img" aria-label="Faint architectural floor-plan line pattern"></div>
  <div class="card__edge card__edge--left"></div>
  <div class="card__edge card__edge--right"></div>
  <div class="brand">
    <span class="brand__mark"></span>
    <span class="brand__name">Maple Fitouts</span>
  </div>
  <p class="front__url">www.maplefitouts-example.com.au</p>
</section>

<section class="card card--back" aria-label="Business card back">
  <div class="card__texture" role="img" aria-label="Faint architectural floor-plan line pattern"></div>
  <svg class="back__panel" viewBox="0 0 230 350" preserveAspectRatio="none" aria-hidden="true">
    <defs>
      <linearGradient id="panelSheen" x1="0" x2="1" y1="0" y2="0">
        <stop offset="0" stop-color="#b9a58a"/>
        <stop offset="0.15" stop-color="#f4eee6"/>
        <stop offset="0.7" stop-color="#e6dccd"/>
        <stop offset="1" stop-color="#c9b79f"/>
      </linearGradient>
    </defs>
    <path d="M30 0 H230 V350 H20 Q-10 175 30 0 Z" fill="url(#panelSheen)"/>
  </svg>
  <div class="brand">
    <span class="brand__mark"></span>
    <span class="brand__name">Maple Fitouts</span>
  </div>

  <h1 class="contact__name">Rowan Pellicott</h1>
  <p class="contact__role">Director</p>

  <div class="contact__address">
    <svg class="icon" viewBox="0 0 14 14" aria-hidden="true"><path d="M7 1 L13 7 H11 V13 H3 V7 H1 Z"/></svg>
    <p>P.O. Box 871<br>Kestrel Bay NSW 2099</p>
  </div>

  <ul class="contact__list">
    <li><svg class="icon" viewBox="0 0 14 14" aria-hidden="true"><path d="M2 4 Q7 0 12 4 L10 6 L8 5 H6 L4 6 Z M3 8 H11 L12 13 H2 Z"/></svg>02 95318274</li>
    <li><svg class="icon" viewBox="0 0 14 14" aria-hidden="true"><rect x="4" y="1" width="6" height="12" rx="1"/></svg>0418593417</li>
    <li><svg class="icon" viewBox="0 0 14 14" aria-hidden="true"><path d="M4 1 H10 V5 H12 V12 H2 V5 H4 Z"/></svg>02 95318291</li>
    <li><svg class="icon" viewBox="0 0 14 14" aria-hidden="true"><path d="M1 3 H13 V11 H1 Z M1 3 L7 8 L13 3" stroke="#e8b000" stroke-width="1"/></svg>rowan@maplefitouts-example.com.au</li>
    <li><svg class="icon icon--blank" viewBox="0 0 14 14" aria-hidden="true"></svg>www.maplefitouts-example.com.au</li>
  </ul>
</section>

</body>
</html>
```